Roofing Company Now Hiring and Call Now Facebook Ads

Trying to hire new sales reps in our Alabama market to add to our growing team. This is a great opportunity for any one looking for a career change or looking to add time back to the time they get to spend at home with their families. This is a chance to build a career in one of the fastest growing industries in the country and build financial freedom and a solid future for your family while easily making 6 figures yearly. Sales reps get to set their own schedule, take vacations when they want, and could even choose if they wanted to work in the summer or the winter seasons if they dont like the heat/cold environment. Sales reps are commission based with bonus/incentives for completing task and assignments weekly.

"Let's Talk About Your Roof!" Schedule a free Roof Inspection today!

Needing facebook ads for hiring and a few ads templates for daily post regarding roof inspections and roof replacements, if they are editable it would be easier for me to manage a few templates. This project needs to have a swag/cleanish look that attracts the younger group of people but still make the older group of customer think, man these guys have some solid looking things going on and looks like a well managed and built company. We also target the upper scale areas when seeking customers.

Lets see what yall got! lets Gooo!

Target Market(s)

Property owners, sales reps, homeowners, property managers, job seekers

Industry/Entity Type

Roofing Contractor Storm Restoration Contractor, Construction Contractor

Font styles to use
Sans Serif

Colors
EB3D1F
EC4F4E
F09395
F8D3D4
FCEDEE

Requirements
Must have
• Clean modern professional look with visible red and black colors, we like white too.
Nice to have
• red, black, white, popping eye catching colors.
Should not have
• wrong color red, red is more of a calder ridge otters red, please stay away from the pinkish red.

```html
<!DOCTYPE html>
<html lang="en">
<head>
<meta charset="utf-8">
<title>Summit Crest Roofing — We are Hiring</title>
<link rel="stylesheet" href="https://fonts.googleapis.com/css2?family=Raleway:wght@300;400;800&display=swap">
<style>
  :root {
    --frame-grey: #9a9b9e;
    --brand-red: #e8401f;
    --brand-red-clear: rgba(232, 64, 31, 0);
    --white: #ffffff;
    --roof-slate: #55606b;
    --roof-shadow: #2c333b;
    --foliage: #95a24a;
    --foliage-deep: #5f6e2c;
    --smoke: #e0a79a;
    --shirt: #e6e8ec;
    --button-glass: rgba(255, 255, 255, 0.3);
  }
  * { margin: 0; padding: 0; box-sizing: border-box; }
  html, body {
    width: 1200px;
    height: 628px;
    overflow: hidden;
    background: var(--frame-grey);
  }
  .ad {
    position: relative;
    width: 1200px;
    height: 628px;
    background: var(--frame-grey);
    font-family: "Raleway", sans-serif;
    color: var(--white);
  }
  .ad__card {
    position: absolute;
    left: 74px;
    top: 38px;
    width: 1052px;
    height: 552px;
    overflow: hidden;
    background: var(--brand-red);
  }
  .ad__photo {
    position: absolute;
    left: 330px;
    top: 0;
    width: 722px;
    height: 552px;
    background:
      radial-gradient(ellipse 30% 30% at 88% 12%, var(--shirt), transparent 75%),
      radial-gradient(ellipse 32% 26% at 28% 8%, var(--smoke), transparent 75%),
      radial-gradient(ellipse 45% 35% at 70% 30%, var(--foliage), transparent 75%),
      linear-gradient(170deg, var(--foliage-deep) 0%, var(--foliage) 22%, var(--roof-slate) 48%, var(--roof-shadow) 100%);
  }
  .ad__fade {
    position: absolute;
    inset: 0;
    background: linear-gradient(90deg, var(--brand-red) 0%, var(--brand-red) 36%, var(--brand-red-clear) 56%);
  }
  .brand {
    position: absolute;
    left: 64px;
    top: 50px;
    width: 140px;
    font-weight: 800;
    font-size: 18px;
    line-height: 1.05;
    letter-spacing: 0.5px;
    text-transform: uppercase;
  }
  .deco { position: absolute; }
  .deco--ring { left: 362px; top: 56px; }
  .deco--wave-top { left: 238px; top: 124px; }
  .deco--wave-low { left: 532px; top: 424px; }
  .headline {
    position: absolute;
    left: 64px;
    top: 150px;
  }
  .headline__lead {
    display: block;
    font-weight: 300;
    font-size: 48px;
    line-height: 1;
  }
  .headline__strong {
    display: block;
    font-weight: 800;
    font-size: 74px;
    line-height: 1;
    margin-top: 8px;
  }
  .headline__join {
    display: block;
    font-weight: 800;
    font-size: 136px;
    line-height: 1;
    margin-top: -14px;
    letter-spacing: -2px;
  }
  .headline__team {
    display: block;
    text-align: right;
    font-weight: 300;
    font-size: 34px;
    line-height: 1;
    margin-top: -18px;
  }
  .tagline {
    position: absolute;
    left: 64px;
    top: 468px;
    font-weight: 400;
    font-size: 33px;
    line-height: 1;
    text-transform: uppercase;
  }
  .cta {
    position: absolute;
    left: 756px;
    top: 472px;
    width: 150px;
    height: 38px;
    border-radius: 6px;
    background: var(--button-glass);
    font-weight: 400;
    font-size: 17px;
    line-height: 38px;
    text-align: center;
  }
</style>
</head>
<body>
<main class="ad">
  <section class="ad__card">
    <div class="ad__photo" role="img" aria-label="Photo of a roofer kneeling on a dark shingle roof using a nail gun with a blue air hose, green trees behind"></div>
    <div class="ad__fade"></div>

    <div class="brand">Summit Crest Roofing</div>

    <svg class="deco deco--ring" width="34" height="34" viewBox="0 0 34 34" aria-hidden="true">
      <circle cx="17" cy="17" r="15" fill="none" stroke="#ffffff" stroke-opacity="0.75" stroke-width="1.5"/>
    </svg>
    <svg class="deco deco--wave-top" width="76" height="26" viewBox="0 0 76 26" aria-hidden="true">
      <path d="M2 8 q9 -7 18 0 t18 0 t18 0 t18 0" fill="none" stroke="#ffffff" stroke-opacity="0.7" stroke-width="1.5"/>
      <path d="M2 18 q9 -7 18 0 t18 0 t18 0 t18 0" fill="none" stroke="#ffffff" stroke-opacity="0.7" stroke-width="1.5"/>
    </svg>
    <svg class="deco deco--wave-low" width="76" height="26" viewBox="0 0 76 26" aria-hidden="true">
      <path d="M2 8 q9 -7 18 0 t18 0 t18 0 t18 0" fill="none" stroke="#ffffff" stroke-opacity="0.7" stroke-width="1.5"/>
      <path d="M2 18 q9 -7 18 0 t18 0 t18 0 t18 0" fill="none" stroke="#ffffff" stroke-opacity="0.7" stroke-width="1.5"/>
    </svg>

    <h1 class="headline">
      <span class="headline__lead">We are</span>
      <span class="headline__strong">Hiring</span>
      <span class="headline__join">JOIN</span>
      <span class="headline__team">OUR TEAM</span>
    </h1>

    <p class="tagline">Be part of our story</p>

    <div class="cta">Read More</div>
  </section>
</main>
</body>
</html>
```